Harbour Vale Lettings Web Site Design

I am after a very simple 3 page web site please. I attach a PDF with the text and information. The logo is also in the PDF. The colours should be orange and blues. The pages should be HOME - LANDLORDS - TENANTS.
Lettings and Property Management Company aimed at just being a reference point for tenants but more of a sales pitch to landlords. Please refer to the attached PDF and word file which contains far more content for the various pages.

Target Market(s)

Prospective Landlords mainly but tenants also

Industry/Entity Type

Lettings and Property Management

Number of Pages Required

3 page

Font styles to use
Sans Serif
Other font styles liked:
• Candara

Colors
0054AA
0677BA
7BADD7
CADEEF
E8F1F8
F0912C
F2A743
F7CA91
FBE8D2
FDF5EE

Requirements
Must have
• Must be colour co-ordinated to the logo (orange and dark blue predominently, Must have good quality stock images relating to property and renting out property. Should have home page and links to landlord page and tenant page. Must have the 4 logos that we are affiliated to (TKR, Tenancy Settle, BNF and Funds Guard Scheme) - all attached.
Nice to have
• Modern feel, crisp and sharp but simple - good stock images.

```html
<!DOCTYPE html>
<html lang="en">
<head>
<meta charset="utf-8">
<title>Harbour Vale Lettings — Lettings and Property Management</title>
<link rel="stylesheet" href="https://fonts.googleapis.com/css2?family=Open+Sans:wght@400;600;700;800&display=swap">
<style>
:root{
  --blue:#0054AA;--blue-mid:#0677BA;--blue-soft:#7BADD7;--blue-pale:#CADEEF;--blue-wash:#E8F1F8;
  --orange:#F0912C;--orange-lt:#F2A743;--peach:#F7CA91;--peach-pale:#FBE8D2;--cream:#FDF5EE;
  --ink:#1d1d1d;--grey:#555;--white:#fff;
}
*{box-sizing:border-box;margin:0;padding:0}
html,body{width:1200px;height:4622px;overflow:hidden}
body{font-family:"Open Sans",Arial,sans-serif;color:var(--ink);background:#fff;position:relative}
.abs{position:absolute}
.btn{position:absolute;display:flex;align-items:center;justify-content:center;font-size:12px;font-weight:700;color:#fff;text-transform:uppercase;border-radius:3px;letter-spacing:.3px}
.btn-orange{background:var(--orange)}
.btn-blue{background:var(--blue)}
.eyebrow{color:var(--orange);font-size:16px;text-align:center}
.section-title{color:var(--blue);font-weight:800;font-size:34px;text-align:center;line-height:1.2}

/* header */
.site-header{position:absolute;left:0;top:0;width:1200px;height:115px;background:#fff}
.brand-panel{position:absolute;left:0;top:0;width:235px;height:115px;background:var(--blue);clip-path:polygon(0 0,100% 0,80% 100%,0 100%)}
.brand-name{position:absolute;left:28px;top:18px;width:170px;color:#fff;font-size:14px;font-weight:600;line-height:1.3;text-align:center}
.brand-dot{display:block;width:30px;height:30px;border-radius:50%;background:var(--orange);margin:0 auto 6px}
.topbar{position:absolute;left:816px;top:0;width:384px;height:40px;background:var(--blue);clip-path:polygon(0 0,100% 0,100% 100%,6% 100%);color:#fff;font-size:11px}
.topbar .item{position:absolute;top:5px;display:flex;gap:8px;align-items:center;line-height:1.25}
.main-nav{position:absolute;top:72px;left:700px;font-size:13px}
.main-nav a{position:absolute;color:var(--ink);text-decoration:none;white-space:nowrap}
.main-nav a.active{color:var(--blue-mid)}

/* hero */
.hero{position:absolute;left:0;top:115px;width:1200px;height:551px;background:linear-gradient(180deg,#5c6f85 0%,#8a8f95 45%,#6d5f4f 80%,#3c3a33 100%)}
.hero-shade{position:absolute;inset:0;background:linear-gradient(90deg,rgba(20,30,45,.55),rgba(20,30,45,.05))}
.hero h1{position:absolute;left:50px;top:148px;font-size:44px;line-height:1.2;font-weight:600;color:#fff}
.hero h1 span{color:var(--orange);font-weight:700;display:block}
.hero p{position:absolute;left:52px;top:278px;width:560px;color:#fff;font-size:15px;line-height:1.5}

/* services */
.services{position:absolute;left:0;top:666px;width:1200px;height:841px}
.service-card{position:absolute;top:213px;width:534px;height:521px;background:var(--blue);color:#fff}
.service-card .photo{height:258px}
.service-card .badge{position:absolute;left:225px;top:212px;width:84px;height:84px;border-radius:50%;background:var(--orange);display:flex;align-items:center;justify-content:center}
.service-card h3{position:absolute;left:22px;top:283px;font-size:19px;font-weight:700}
.service-card p{position:absolute;left:22px;top:323px;width:496px;font-size:12.5px;line-height:1.6}

/* about */
.about{position:absolute;left:0;top:1507px;width:1200px;height:553px;background:var(--blue-wash);overflow:hidden}
.about-wedge{position:absolute;left:0;top:0;width:470px;height:553px;background:var(--orange);clip-path:polygon(0 0,100% 0,10% 100%,0 100%)}
.about-photo{position:absolute;left:68px;top:98px;width:443px;height:345px;border:3px solid var(--blue);background:linear-gradient(135deg,#c9b89e,#8b7a66 55%,#4a5f7e)}
.stat{position:absolute;width:96px;height:92px;background:#fff;border-radius:4px;padding:10px}
.stat b{display:block;font-size:32px;color:var(--blue);line-height:1}
.stat small{display:block;font-size:12px;color:var(--grey);line-height:1.2;margin-top:2px}
.about-text{position:absolute;left:558px;top:100px;width:590px}
.about-text .eyebrow{text-align:left}
.about-text h2{color:var(--blue);font-size:35px;font-weight:800;display:flex;align-items:center;gap:8px;margin:2px 0 14px}
.about-text p{font-size:12.5px;line-height:1.55;margin-bottom:16px;color:#333}

/* properties */
.properties{position:absolute;left:0;top:2060px;width:1200px;height:873px;background:#f7f7f8}
.prop-card{position:absolute;top:252px;width:346px;height:424px;background:#fff;box-shadow:0 2px 10px rgba(0,0,0,.08)}
.prop-card .photo{height:205px}
.prop-card .addr{position:absolute;left:16px;top:225px;font-size:14px;color:#444;display:flex;gap:8px;align-items:center}
.prop-card h3{position:absolute;left:16px;top:254px;font-size:20px;font-weight:800;line-height:1.2;color:var(--ink)}
.prop-card h3.blue{color:var(--blue)}
.prop-card .feats{position:absolute;left:14px;top:322px;display:flex;gap:18px;font-size:14px;color:#555}
.prop-card .feats span{display:flex;gap:5px;align-items:center}
.prop-card .price{position:absolute;left:16px;top:373px;font-size:17px;font-weight:700;color:var(--blue)}
.prop-card .price small{font-size:14px;font-weight:400;color:#666}
.fav{position:absolute;right:16px;top:364px;width:36px;height:36px;border-radius:50%;display:flex;align-items:center;justify-content:center}
.fav.fill{background:var(--orange)}
.fav.line{border:2px solid var(--orange);background:#fff}

/* testimonial */
.testimonial{position:absolute;left:0;top:2933px;width:1200px;height:542px;background:var(--cream)}
.quote-mark{position:absolute;left:112px;top:0;font-size:190px;line-height:1;color:var(--peach);font-weight:800;font-family:Georgia,serif}
.testimonial h2{position:absolute;left:118px;top:207px;font-size:25px;font-weight:800;line-height:1.3}
.testimonial p{position:absolute;left:118px;top:290px;width:360px;font-size:12px;line-height:1.55;color:#333}
.testimonial .who{position:absolute;left:118px;top:362px;font-size:13px;color:var(--orange)}
.testimonial .where{position:absolute;left:118px;top:380px;font-size:12px;color:#444}
.dots{position:absolute;left:118px;top:411px;display:flex;gap:5px}
.dots i{width:10px;height:10px;border-radius:50%;background:var(--peach)}
.dots i:first-child{background:var(--orange)}
.t-frame{position:absolute;left:533px;top:72px;width:590px;height:396px;border:1.5px solid #777}
.t-photo{position:absolute;left:520px;top:101px;width:558px;height:375px;background:linear-gradient(135deg,#c7c9cc,#aeb1b5 55%,#e8e4e0)}

/* contact */
.contact{position:absolute;left:0;top:3475px;width:1200px;height:773px}
.deco-top{position:absolute;left:960px;top:90px;width:188px;height:330px;background:var(--blue-pale)}
.deco-bot{position:absolute;left:52px;top:130px;width:188px;height:403px;background:var(--blue-pale)}
.contact-box{position:absolute;left:70px;top:113px;width:1060px;height:431px;background:var(--blue);overflow:hidden}
.contact-box .scene{position:absolute;right:0;bottom:0;width:420px;height:300px;background:linear-gradient(180deg,rgba(255,255,255,0),rgba(255,255,255,.08))}
.contact-box h2{position:absolute;left:0;width:100%;top:60px;text-align:center;color:#fff;font-size:34px;font-weight:700}
.field{position:absolute;background:#fff;border-radius:4px;font-size:12px;color:#666;display:flex;align-items:center;gap:6px;padding:0 8px}
.field.area{align-items:flex-start;padding-top:10px}

/* accreditation strip */
.partners{position:absolute;left:135px;top:4094px;width:929px;height:172px;background:#fff;box-shadow:0 2px 14px rgba(0,0,0,.08);z-index:2}
.partners .arrow{position:absolute;top:68px;width:38px;height:38px;border-radius:50%;border:2px solid var(--blue);display:flex;align-items:center;justify-content:center}
.partner-row{position:absolute;left:78px;top:0;width:773px;height:172px;display:flex;align-items:center;justify-content:space-around}
.partner{font-size:20px;font-weight:600;color:var(--grey);white-space:nowrap}

/* footer */
.site-footer{position:absolute;left:0;top:4248px;width:1200px;height:344px;background:var(--blue);color:#fff}
.f-brand{position:absolute;left:52px;top:120px;width:230px;text-align:center;font-size:24px;font-weight:600;line-height:1.2}
.f-brand .dot{display:block;width:70px;height:70px;border-radius:50%;background:var(--orange);margin:0 auto 16px}
.social{position:absolute;left:56px;top:280px;display:flex;gap:14px}
.social i{width:28px;height:28px;border-radius:50%;background:#fff}
.social i:first-child{background:var(--orange);border:2px solid #fff}
.f-col{position:absolute;top:67px;font-size:12.5px;line-height:29px}
.f-col h4{font-size:12.5px;font-weight:700;line-height:26px}
.f-contact div{display:flex;gap:10px;align-items:flex-start;line-height:1.4;margin-bottom:12px}
.copyright{position:absolute;left:0;top:4592px;width:1200px;height:30px;background:var(--blue);border-top:1px solid rgba(255,255,255,.25);color:#fff;font-size:12px;text-align:center;line-height:30px}
</style>
</head>
<body>

<header class="site-header">
  <div class="brand-panel"></div>
  <div class="brand-name"><span class="brand-dot"></span>Harbour Vale Lettings</div>
  <div class="topbar">
    <div class="item" style="left:28px">
      <svg width="22" height="22" viewBox="0 0 24 24" fill="none" stroke="#fff" stroke-width="1.6"><path d="M5 3h4l2 5-3 2a12 12 0 0 0 6 6l2-3 5 2v4a2 2 0 0 1-2 2A17 17 0 0 1 3 5a2 2 0 0 1 2-2z"/></svg>
      <div>Call us<br><b>0201 555 0148</b></div>
    </div>
    <div class="item" style="left:155px">
      <svg width="26" height="20" viewBox="0 0 26 20" fill="none" stroke="#fff" stroke-width="1.6"><rect x="1" y="1" width="24" height="18" rx="1"/><path d="M1 2l12 9 12-9"/></svg>
      <div>Email<br>hello@harbourvale.example</div>
    </div>
  </div>
  <nav class="main-nav">
    <a class="active" href="#" style="left:0;top:0">
      <svg width="18" height="14" viewBox="0 0 24 18" style="position:absolute;left:12px;top:-16px"><path d="M12 1L2 9h3v8h14V9h3z" fill="var(--blue)"/></svg>Home</a>
    <a href="#" style="left:80px">About</a>
    <a href="#" style="left:160px">Land Lord</a>
    <a href="#" style="left:266px">Tenent</a>
  </nav>
  <span class="btn btn-orange" style="left:1048px;top:63px;width:100px;height:34px;font-size:13px">Contact</span>
</header>

<section class="hero">
  <div role="img" aria-label="Modern white villa with large glass windows at dusk" style="position:absolute;inset:0"></div>
  <div class="hero-shade"></div>
  <h1><span>LETTINGS AND PROPERTY</span>MANAGEMENT COMPANY</h1>
  <p>Aimed at just being a reference point for tenants but more of a sales pitch to landlords</p>
  <span class="btn btn-blue" style="left:52px;top:357px;width:175px;height:34px">Landlord Enquiry</span>
  <span class="btn btn-orange" style="left:257px;top:357px;width:140px;height:34px">Contact &nbsp;Now</span>
</section>

<section class="services">
  <svg class="abs" style="left:586px;top:68px" width="28" height="26" viewBox="0 0 24 22"><path d="M12 1L1 10h3v11h16V10h3z" fill="var(--blue)"/><rect x="9" y="13" width="6" height="8" fill="#fff"/></svg>
  <div class="eyebrow abs" style="left:0;width:1200px;top:100px">What We Do</div>
  <h2 class="section-title abs" style="left:0;width:1200px;top:120px">OUR SERVICES</h2>

  <article class="service-card" style="left:52px">
    <div class="photo" role="img" aria-label="Grey clapboard family house with front lawn" style="background:linear-gradient(180deg,#9bb6c9,#8e9499 50%,#5f7a48)"></div>
    <div class="badge"><svg width="40" height="40" viewBox="0 0 24 24" fill="none" stroke="#fff" stroke-width="1.5"><path d="M3 11L12 4l9 7"/><path d="M5 10v10h14V10"/><circle cx="12" cy="13" r="2"/><path d="M9 19c0-2 1.5-3 3-3s3 1 3 3"/></svg></div>
    <h3>LANDLORDS</h3>
    <p>Whether you are an experienced landlord with a large portfolio or looking to take your first steps into the buy to let market, or maybe you’ve inherited a property and have no idea what to do with it, we are here to make life easier for you every step of the way of your property management in Eastbourne and the surrounding area.</p>
    <span class="btn btn-orange" style="left:22px;top:444px;width:128px;height:34px;font-size:11px">Read More</span>
  </article>

  <article class="service-card" style="left:615px">
    <div class="photo" role="img" aria-label="White modern house with pool and terrace" style="background:linear-gradient(180deg,#d8e3ea,#e9ecee 45%,#7f8a78 80%,#3f6b7d)"></div>
    <div class="badge"><svg width="40" height="40" viewBox="0 0 24 24" fill="none" stroke="#fff" stroke-width="1.5"><path d="M3 16l4-1 5 2 6-4a1.5 1.5 0 0 0-2-2l-4 2"/><path d="M3 20l5-1 6 1"/><path d="M14 4l6 5-5 5-5-5z"/></svg></div>
    <h3>TENANTS</h3>
    <p>Start your renting journey with Harbour Vale Lettings for a seamless renting experience and complete peace of mind.<br>Let’s find you a place to call home whether you’re looking for somewhere temporary or a place to put down roots, we can help</p>
    <span class="btn btn-orange" style="left:22px;top:444px;width:128px;height:34px;font-size:11px">Read More</span>
  </article>
</section>

<section class="about">
  <div class="about-wedge"></div>
  <div class="about-photo" role="img" aria-label="Father and child sitting outside a new home holding a cardboard roof"></div>
  <div class="stat" style="left:398px;top:125px"><b>20+</b><small>Years of Expereince</small></div>
  <div class="stat" style="left:398px;top:227px"><b>£75</b><small>Per month Charge</small></div>
  <div class="stat" style="left:398px;top:329px"><b>24/7</b><small>Emergency Service</small></div>
  <div class="about-text">
    <div class="eyebrow">About Us</div>
    <h2>HARBOUR VALE LETTINGS <svg width="30" height="28" viewBox="0 0 24 22"><path d="M12 1L1 10h3v11h16V10h3z" fill="var(--blue)"/><rect x="9" y="13" width="6" height="8" fill="#fff"/></svg></h2>
    <p>Harbour Vale Lettings has emerged after over 20 years of privately managing our own rental properties. We are family run and decided to move all of our properties under one ‘umbrella’. Now professionally set up as a legal entity, Harbour Vale is looking to welcome new tenants and landlords to an innovative and fresh way of letting property.</p>
    <p>We always maintain a high standard of service and our friendly and helpful team are experienced in all areas and offer an excellent service in helping landlords and tenants deal with problems and issues they face daily.</p>
    <p>Out of hours emergency service which means we are there (in an emergency) for our tenants and landlords 24/7.</p>
  </div>
  <span class="btn btn-blue" style="left:556px;top:410px;width:127px;height:34px">Read More</span>
</section>

<section class="properties">
  <svg class="abs" style="left:586px;top:75px" width="28" height="26" viewBox="0 0 24 22"><path d="M12 1L1 10h3v11h16V10h3z" fill="var(--blue)"/><rect x="9" y="13" width="6" height="8" fill="#fff"/></svg>
  <div class="eyebrow abs" style="left:0;width:1200px;top:108px">Latest Properties</div>
  <h2 class="section-title abs" style="left:0;width:1200px;top:130px">EXPLORE FEATURED<br>PROPERTIES</h2>

  <article class="prop-card" style="left:52px">
    <div class="photo" role="img" aria-label="Grey family house with gables and lawn" style="background:linear-gradient(180deg,#c9d5de,#8d9593 55%,#6a8a4e)"></div>
    <div class="addr"><svg width="14" height="18" viewBox="0 0 14 18"><path d="M7 1a6 6 0 0 1 6 6c0 4-6 10-6 10S1 11 1 7a6 6 0 0 1 6-6z" fill="none" stroke="var(--orange)" stroke-width="1.8"/><circle cx="7" cy="7" r="2" fill="var(--orange)"/></svg>Marlow Court 12b, Harbourton</div>
    <h3 class="blue">SUPER DELUXE HOUSE<br>NEAR SEA BEECH</h3>
    <div class="feats">
      <span><svg width="22" height="14" viewBox="0 0 22 14" fill="none" stroke="var(--orange)" stroke-width="1.4"><path d="M1 13V2M1 8h20v5M3 8V5h7v3"/></svg>4 Beds</span>
      <span><svg width="22" height="16" viewBox="0 0 22 16" fill="none" stroke="var(--orange)" stroke-width="1.4"><path d="M1 8h20v3a4 4 0 0 1-4 4H5a4 4 0 0 1-4-4zM4 8V3a2 2 0 0 1 4 0"/></svg>2 Bathrooms</span>
      <span><svg width="16" height="16" viewBox="0 0 16 16" fill="none" stroke="var(--orange)" stroke-width="1.4"><path d="M2 1v13h13M5 11l8-8M9 3h4v4"/></svg>6x8 m²</span>
    </div>
    <div class="price">$2,400 <small>/month</small></div>
    <div class="fav fill"><svg width="16" height="14" viewBox="0 0 16 14"><path d="M8 13L2 7a3.5 3.5 0 0 1 6-4 3.5 3.5 0 0 1 6 4z" fill="#fff"/></svg></div>
  </article>

  <article class="prop-card" style="left:427px">
    <div class="photo" role="img" aria-label="Contemporary two storey house with lit windows" style="background:linear-gradient(180deg,#e3e8ec,#a38d77 55%,#5d7a45)"></div>
    <div class="addr"><svg width="14" height="18" viewBox="0 0 14 18"><path d="M7 1a6 6 0 0 1 6 6c0 4-6 10-6 10S1 11 1 7a6 6 0 0 1 6-6z" fill="none" stroke="var(--orange)" stroke-width="1.8"/><circle cx="7" cy="7" r="2" fill="var(--orange)"/></svg>Marlow Court 12b, Harbourton</div>
    <h3>SUPER DELUXE HOUSE<br>NEAR SEA BEECH</h3>
    <div class="feats">
      <span><svg width="22" height="14" viewBox="0 0 22 14" fill="none" stroke="var(--orange)" stroke-width="1.4"><path d="M1 13V2M1 8h20v5M3 8V5h7v3"/></svg>4 Beds</span>
      <span><svg width="22" height="16" viewBox="0 0 22 16" fill="none" stroke="var(--orange)" stroke-width="1.4"><path d="M1 8h20v3a4 4 0 0 1-4 4H5a4 4 0 0 1-4-4zM4 8V3a2 2 0 0 1 4 0"/></svg>2 Bathrooms</span>
      <span><svg width="16" height="16" viewBox="0 0 16 16" fill="none" stroke="var(--orange)" stroke-width="1.4"><path d="M2 1v13h13M5 11l8-8M9 3h4v4"/></svg>6x8 m²</span>
    </div>
    <div class="price">$2,400 <small>/month</small></div>
    <div class="fav line"><svg width="16" height="14" viewBox="0 0 16 14"><path d="M8 13L2 7a3.5 3.5 0 0 1 6-4 3.5 3.5 0 0 1 6 4z" fill="var(--orange)"/></svg></div>
  </article>

  <article class="prop-card" style="left:802px">
    <div class="photo" role="img" aria-label="Modern house glowing at twilight" style="background:linear-gradient(180deg,#1f3552,#3a4a66 50%,#c9914f 75%,#2e3a2e)"></div>
    <div class="addr"><svg width="14" height="18" viewBox="0 0 14 18"><path d="M7 1a6 6 0 0 1 6 6c0 4-6 10-6 10S1 11 1 7a6 6 0 0 1 6-6z" fill="none" stroke="var(--orange)" stroke-width="1.8"/><circle cx="7" cy="7" r="2" fill="var(--orange)"/></svg>Marlow Court 12b, Harbourton</div>
    <h3>SUPER DELUXE HOUSE<br>NEAR SEA BEECH</h3>
    <div class="feats">
      <span><svg width="22" height="14" viewBox="0 0 22 14" fill="none" stroke="var(--orange)" stroke-width="1.4"><path d="M1 13V2M1 8h20v5M3 8V5h7v3"/></svg>4 Beds</span>
      <span><svg width="22" height="16" viewBox="0 0 22 16" fill="none" stroke="var(--orange)" stroke-width="1.4"><path d="M1 8h20v3a4 4 0 0 1-4 4H5a4 4 0 0 1-4-4zM4 8V3a2 2 0 0 1 4 0"/></svg>2 Bathrooms</span>
      <span><svg width="16" height="16" viewBox="0 0 16 16" fill="none" stroke="var(--orange)" stroke-width="1.4"><path d="M2 1v13h13M5 11l8-8M9 3h4v4"/></svg>6x8 m²</span>
    </div>
    <div class="price">$2,400 <small>/month</small></div>
    <div class="fav line"><svg width="16" height="14" viewBox="0 0 16 14"><path d="M8 13L2 7a3.5 3.5 0 0 1 6-4 3.5 3.5 0 0 1 6 4z" fill="var(--orange)"/></svg></div>
  </article>

  <span class="btn btn-blue" style="left:537px;top:726px;width:127px;height:36px">Explore More</span>
</section>

<section class="testimonial">
  <div class="quote-mark">“</div>
  <h2>WHAT OUR<br>COMMUNITY IS SAYING</h2>
  <p>This was by far and away the best experience I have had with an estate agency. Lovely people and above all supremely professional with both me as a seller and the buyers.</p>
  <div class="who">MARIANNE</div>
  <div class="where">Battersea office</div>
  <div class="dots"><i></i><i></i><i></i></div>
  <div class="t-frame"></div>
  <div class="t-photo" role="img" aria-label="Portrait of a smiling client in a white blouse"></div>
</section>

<section class="contact">
  <div class="deco-top"></div>
  <div class="deco-bot"></div>
  <div class="contact-box">
    <div class="scene" role="img" aria-label="Faint street of houses behind the form"></div>
    <svg class="abs" style="left:516px;top:20px" width="28" height="26" viewBox="0 0 24 22"><path d="M12 1L1 10h3v11h16V10h3z" fill="#fff"/><rect x="9" y="13" width="6" height="8" fill="var(--blue)"/></svg>
    <h2>GET IN TOUCH WITH US</h2>
    <div class="field" style="left:249px;top:122px;width:275px;height:42px">
      <svg width="12" height="12" viewBox="0 0 12 12" fill="none" stroke="#666"><circle cx="6" cy="4" r="2.5"/><path d="M1 11c0-3 2.5-4 5-4s5 1 5 4"/></svg>Name</div>
    <div class="field" style="left:538px;top:122px;width:271px;height:42px">
      <svg width="12" height="12" viewBox="0 0 12 12" fill="none" stroke="#666"><circle cx="6" cy="4" r="2.5"/><path d="M1 11c0-3 2.5-4 5-4s5 1 5 4"/></svg>Last Name</div>
    <div class="field" style="left:249px;top:185px;width:275px;height:42px">
      <svg width="12" height="12" viewBox="0 0 24 24" fill="none" stroke="#666" stroke-width="2"><path d="M5 3h4l2 5-3 2a12 12 0 0 0 6 6l2-3 5 2v4a2 2 0 0 1-2 2A17 17 0 0 1 3 5a2 2 0 0 1 2-2z"/></svg>Phone</div>
    <div class="field" style="left:538px;top:185px;width:271px;height:42px">
      <svg width="13" height="10" viewBox="0 0 26 20" fill="none" stroke="#666" stroke-width="2"><rect x="1" y="1" width="24" height="18"/><path d="M1 2l12 9 12-9"/></svg>Email</div>
    <div class="field area" style="left:249px;top:249px;width:560px;height:72px">
      <svg width="12" height="12" viewBox="0 0 12 12" fill="none" stroke="#666"><path d="M6 1a5 5 0 1 1-3 9l-2 1 1-2A5 5 0 0 1 6 1z"/></svg>Leave Message</div>
    <span class="btn btn-orange" style="left:481px;top:352px;width:124px;height:34px;border-radius:17px">Send Now</span>
  </div>
</section>

<div class="partners" aria-label="Accreditations">
  <div class="arrow" style="left:20px"><svg width="10" height="14" viewBox="0 0 10 14" fill="none" stroke="var(--ink)" stroke-width="2"><path d="M8 1L2 7l6 6"/></svg></div>
  <div class="partner-row">
    <span class="partner">Tenancy Settle</span>
    <span class="partner">Funds Guard Scheme</span>
    <span class="partner">TKR</span>
    <span class="partner">BNF</span>
  </div>
  <div class="arrow" style="right:20px"><svg width="10" height="14" viewBox="0 0 10 14" fill="none" stroke="var(--blue)" stroke-width="2"><path d="M2 1l6 6-6 6"/></svg></div>
</div>

<footer class="site-footer">
  <div class="f-brand"><span class="dot"></span>Harbour Vale<br>Lettings</div>
  <div class="social" aria-label="Social links"><i></i><i></i><i></i></div>
  <div class="f-col" style="left:427px"><h4>NAVIGATION</h4>Home<br>About<br>Land Lord<br>Tenent</div>
  <div class="f-col" style="left:615px"><h4>FEES &amp; CHARGES</h4>Tanent Fees (AST)<br>Land lord Fees (Non AST )<br>Land Lord</div>
  <div class="f-col f-contact" style="left:895px;line-height:1.4">
    <h4 style="margin-bottom:6px">CONTACT US</h4>
    <div><svg width="16" height="22" viewBox="0 0 14 18"><path d="M7 1a6 6 0 0 1 6 6c0 4-6 10-6 10S1 11 1 7a6 6 0 0 1 6-6z" fill="var(--orange)"/><circle cx="7" cy="7" r="2" fill="var(--blue)"/></svg><span>18 Quayside Row,<br>Harbourton, HV2 4LT</span></div>
    <div><svg width="18" height="18" viewBox="0 0 24 24"><path d="M5 3h4l2 5-3 2a12 12 0 0 0 6 6l2-3 5 2v4a2 2 0 0 1-2 2A17 17 0 0 1 3 5a2 2 0 0 1 2-2z" fill="var(--orange)"/></svg><b>0201-555-0193</b></div>
    <div><svg width="20" height="15" viewBox="0 0 26 20"><rect x="1" y="1" width="24" height="18" fill="var(--orange)"/><path d="M1 2l12 9 12-9" fill="none" stroke="var(--blue)" stroke-width="2"/></svg><b style="text-decoration:underline">hello@harbourvale.example</b></div>
  </div>
</footer>
<div class="copyright">Copyright © 2024 Harbour Vale Lettings All Rights Reserved</div>

</body>
</html>
```